Menu: A4 (double sided) Lunch/Dinner Menu (one side) + Pizza Menu (other side)

Hello.
We would like to create a new style of menus.
Must be easy to read - a summer feel, crisp, clean, beachy, possible retro feel, colours probably based on our website colours (see address below).
Simple and casual is best as we are a casual beachside Cafe.
This menu will be double sided therefore this job is 2 pages.
If you win this job we will have 2 or 3 more menus for you to create soon after (Drinks, Breakfast, possibly a small Kids menu).
The paper for these menus we expect will be a nice white paper which will then be matte laminated.
Colours possible are the green colour #3a6066, the terracotta on our website logo border and website buttons, maybe a little yellow but must be easy to read on white paper.
Black for text might be okay if this is your best design option.
Please view our website and take a feel for the business, location, the existing website branding and website colours we are trying to achieve, www.tidelinekitchen.com.au
We prefer to avoid overwhelming the guest with too many colours on the menus (hence the white paper) as the building is so colourful (El Prado, Argentina, inspired) and the guest experience can be complimented via crisp easy to read menus.
IMPORTANT:
The menus provided please must be fully and easily editable by us in the future.
If you win the job, you must please provide clear instructions on how our staff can edit the menus in the future if project is delivered in Adobe format. Word is also an option for us if you like.
As such, we have attached some documents: the 2x Word documents for the text, 2x .pdf so you can see the fonts and style we were using previously (was printing on recycled brown paper then matte laminated).
If you wished to use the SeaLife Font (this is the existing Font for headings) please let us know as we purchased that font and can provide it.
We have also attached a menu from Marlowe Tavern which we feel has a nice retro feel.
Please include our Instagram in 1 place on the menu @tidelinekitchen
Finally, please note,
we never wish to waste anyone's time so we will narrow down the submissions quickly based on first drafts (please know this is because we appreciate your effort and know your time is valuable) and we will then work with the top designer to finalise in a professional fashion.
Thank you.

```html
<!DOCTYPE html>
<html lang="en">
<head>
<meta charset="utf-8">
<title>Tideline Kitchen — Lunch + Dinner and Pizza Menus</title>
<link href="https://fonts.googleapis.com/css2?family=Londrina+Solid:wght@400;900&family=Titan+One&family=Cormorant+Garamond:wght@600;700&family=Caveat:wght@500;600&family=Nunito:wght@600;700&display=swap" rel="stylesheet">
<style>
  :root {
    --navy: #1f3f73;
    --sea: #2f7fc1;
    --foam: #cfe6f3;
    --sun: #f0dc1a;
    --chilli: #d42a1f;
    --ink: #141414;
    --paper: #ffffff;
    --backdrop: #e6eef1;
    --shop-blue: #1fa3d8;
    --shop-teal: #17938f;
  }
  * { box-sizing: border-box; margin: 0; padding: 0; }
  html, body { width: 1200px; height: 1070px; overflow: hidden; background: var(--backdrop); }
  .spread { position: relative; width: 1200px; height: 1070px; }
  .page {
    position: absolute; top: 132px; width: 570px; height: 806px;
    background: var(--paper); overflow: hidden;
    box-shadow: 0 2px 10px rgba(0,0,0,.12);
  }
  .page--lunch { left: 20px; }
  .page--pizza { left: 610px; }
  .edge-band { position: absolute; left: 0; width: 100%; height: 28px; background: var(--navy); }
  .edge-band--top { top: 0; }
  .edge-band--bottom { bottom: 0; }
  .page-title {
    position: absolute; left: 24px; top: 38px;
    font-family: "Londrina Solid", sans-serif; font-weight: 900;
    color: var(--navy); font-size: 54px; line-height: 48px; letter-spacing: 1px;
  }
  .food-art { position: absolute; border-radius: 50%; background: radial-gradient(circle, #f7f2e6 45%, #f4a76b 46%, #e9e3d4 70%); }
  .shop-art { position: absolute; background: linear-gradient(180deg, var(--navy) 0 10%, var(--shop-blue) 10% 55%, var(--shop-teal) 55% 100%); }
  .social { position: absolute; display: flex; align-items: center; gap: 6px;
    font-family: "Nunito", sans-serif; font-weight: 600; font-size: 17px; color: var(--navy); }
  .social-dot { width: 16px; height: 16px; border-radius: 50%; background: var(--navy); }
  .legend-band { position: absolute; left: 0; width: 100%; height: 34px;
    background: linear-gradient(180deg, #e7f3fa, var(--foam) 50%, #e7f3fa); }
  .legend { position: absolute; left: 36px; top: 9px; font-family: "Nunito", sans-serif;
    font-size: 14px; color: var(--navy); white-space: nowrap; }
  .legend .veg-mark, .veg { color: var(--chilli); font-family: "Caveat", cursive; font-weight: 600; }
  .legend .gfo-mark, .gfo { color: var(--sea); font-family: "Nunito", sans-serif; font-weight: 700; }
  .legend span { margin-right: 6px; }
  .legend .gap { margin-left: 16px; }

  .section-head { position: absolute; font-family: "Titan One", sans-serif; color: var(--sun); letter-spacing: 1px; }
  .section-head--vertical { transform: rotate(-90deg); transform-origin: left top; font-size: 15px; }

  .entree-list { position: absolute; left: 120px; top: 176px; width: 350px; list-style: none; }
  .entree-list li { height: 15.6px; display: flex; align-items: baseline; gap: 4px; white-space: nowrap;
    font-family: "Cormorant Garamond", serif; font-weight: 700; font-size: 11.5px; color: var(--navy); }
  .price-col { position: absolute; list-style: none; font-family: "Cormorant Garamond", serif;
    font-weight: 700; font-size: 10px; color: var(--ink); text-align: right; }
  .price-col li { height: 15.6px; }
  .note { font-family: "Caveat", cursive; font-weight: 500; font-size: 10.5px; color: var(--navy); }
  .chilli { color: var(--chilli); font-size: 10px; }

  .dish-list { position: absolute; left: 26px; width: 500px; list-style: none; }
  .dish { position: relative; margin-bottom: 9px; font-family: "Cormorant Garamond", serif;
    font-weight: 700; font-size: 10.5px; color: var(--ink); text-transform: uppercase; white-space: nowrap; }
  .dish .note { text-transform: none; color: var(--ink); margin-left: 4px; }
  .dish .extra { display: block; padding-left: 260px; margin-top: -2px; text-transform: none;
    font-family: "Caveat", cursive; font-weight: 500; font-size: 10.5px; }
  .dish .price { position: absolute; right: -2px; top: -8px; font-size: 10px; }
  .platter-desc { position: absolute; left: 26px; top: 524px; width: 460px;
    font-family: "Caveat", cursive; font-weight: 500; font-size: 10.5px; line-height: 11px; color: var(--navy); }
  .platter-price { position: absolute; right: 44px; top: 518px; font-family: "Cormorant Garamond", serif; font-weight: 700; font-size: 10px; }
  .cook-note { position: absolute; left: 0; width: 100%; top: 594px; text-align: center;
    font-family: "Caveat", cursive; font-size: 11px; color: var(--navy); }
  .turn-over { position: absolute; right: 28px; bottom: 40px; display: flex; align-items: center; gap: 4px;
    font-family: "Caveat", cursive; font-weight: 600; font-size: 11px; color: var(--sun); }

  .pizza-sub { position: absolute; left: 24px; top: 104px; width: 230px;
    font-family: "Nunito", sans-serif; font-size: 11px; line-height: 13px; color: var(--navy); }
  .allergy-head { position: absolute; left: 36px; top: 190px; font-family: "Titan One", sans-serif;
    font-size: 17px; color: var(--sun); letter-spacing: .5px; }
  .allergy-text { position: absolute; left: 36px; top: 214px; width: 500px;
    font-family: "Cormorant Garamond", serif; font-weight: 600; font-size: 11px; line-height: 12.5px; color: var(--ink); }
  .sides { position: absolute; left: 36px; top: 278px; font-family: "Nunito", sans-serif;
    font-size: 14px; color: var(--sea); white-space: nowrap; }
  .sides b { color: var(--sea); margin: 0 8px; font-weight: 600; }
  .pizza-list { position: absolute; left: 36px; top: 318px; width: 500px; list-style: none; }
  .pizza-list .dish { margin-bottom: 14px; }
  .group-price { position: absolute; font-family: "Cormorant Garamond", serif; font-weight: 700; font-size: 10px; color: var(--ink); }
</style>
</head>
<body>
<main class="spread">

  <!-- Lunch + Dinner side -->
  <section class="page page--lunch" aria-label="Lunch and dinner menu">
    <div class="edge-band edge-band--top"></div>
    <h1 class="page-title">LUNCH+<br>DINNER</h1>
    <div class="food-art" role="img" aria-label="Illustration of a plate with salmon, lemon and salad" style="left:205px; top:40px; width:76px; height:76px;"></div>
    <div class="shop-art" role="img" aria-label="Illustration of the colourful cafe shopfront" style="left:290px; top:18px; width:190px; height:80px;"></div>
    <div class="social" style="left:318px; top:100px;"><span class="social-dot"></span>@tidelinekitchen</div>

    <div class="legend-band" style="top:130px;">
      <p class="legend"><span class="veg-mark">v</span><span>Vegetarian</span><span class="gfo-mark gap">gfo</span><span>Gluten Friendly Optional, please ask</span></p>
    </div>

    <h2 class="section-head section-head--vertical" style="left:86px; top:312px;">ENTREE</h2>
    <ul class="entree-list">
      <li>Garlic Bread (2) <span class="veg">v</span></li>
      <li>Salt &amp; Pepper Squid <span class="note">w/ thai dipping sauce</span></li>
      <li>Duo of Dip <span class="veg">v</span> <span class="note">w/ pita</span></li>
      <li>Bowl of Chips <span class="veg">v</span> <span class="note">w/ tomato sauce</span></li>
      <li>Seasoned Wedges <span class="veg">v</span> <span class="note">w/ sour cream &amp; sweet chilli</span></li>
      <li>Onion Rings (12) <span class="veg">v</span> <span class="note">beer battered w/ tangy mayo</span></li>
      <li>Vietnamese Spring Rolls (3) <span class="note">chicken, home-made</span></li>
      <li>Bruschetta (1) <span class="veg">v</span> <span class="note">w/ olive oil, tomato &amp; red onion salsa, balsamic glaze, feta</span></li>
    </ul>
    <ul class="price-col" style="left:470px; top:168px; width:20px;">
      <li>8</li><li>18</li><li>14</li><li>11</li><li>15</li><li>15</li><li>11</li><li>10</li>
    </ul>

    <h2 class="section-head" style="left:26px; top:316px; font-size:17px;">MAINS</h2>
    <ul class="dish-list" style="top:348px;">
      <li class="dish">The Fish &amp; Chips<span class="note">house-crumbed butterfish w/ chips, tartare &amp; side salad</span><span class="price">25</span></li>
      <li class="dish">Smokey Beef &amp; Bacon Cheese Burger<span class="note">w/ chips, onion rings, gerkins &amp; tangy mayo</span><span class="extra">+ pineapple 2 &nbsp; + jalapenos 2</span><span class="price">23</span></li>
      <li class="dish">Salt &amp; Pepper Squid<span class="note">golden tangles w/ chips, thai dipping sauce &amp; side salad</span><span class="price">31</span></li>
      <li class="dish">Seafood Basket<span class="note">crumbed butterfish, grilled prawns, salt &amp; pepper squid, chips, tartare &amp; side salad</span><span class="price">31</span></li>
      <li class="dish">Atlantic Salmon<span class="note">served w/ mash, teriyaki sauce &amp; winter vegetables &nbsp; (contains breadcrumbs)</span><span class="price">31</span></li>
      <li class="dish">Chicken Parmigiana<span class="note">house-crumbed breast schnitzel, napoli sauce, mozzarella, chips &amp; side salad</span><span class="extra">+ bacon and pineapple 4 &nbsp; + jalapenos and pineapple 4</span><span class="price">27</span></li>
    </ul>

    <h2 class="section-head" style="left:26px; top:500px; font-size:19px;">TIDELINE PLATTER FOR 2</h2>
    <p class="platter-desc">beer battered flathead, salt &amp; pepper squid, prawn skewers, grilled chicken, lamb &amp; chorizo,<br>served with antipasto, dipping sauces, pita &amp; garlic bread &nbsp;90 &nbsp;(+45 pp)</p>
    <ul class="dish-list" style="top:556px;">
      <li class="dish">New York Sirloin <span class="gfo">gfo</span><span class="note">400g MSA w/ mash &amp; winter vegetables &nbsp; or surf 'n' turf <span class="gfo">gfo</span> +6</span><span class="extra" style="padding-left:120px;">choose: mushroom gravy or classic</span><span class="price">38</span></li>
    </ul>
    <p class="cook-note">Please allow 35+ minutes for "well-done"</p>
    <ul class="dish-list" style="top:624px;">
      <li class="dish" style="margin-bottom:12px;">Chicken Caesar<span class="note">w/ bacon, anchovies, egg, caesar dressing, parmesan, spanish onion, garlic bread</span><span class="price">27</span></li>
      <li class="dish" style="margin-bottom:12px;">Lamb Salad <span class="gfo">gfo</span><span class="note">skewers w/ traditional greek salad, tzatziki &amp; garlic bread</span><span class="extra" style="padding-left:150px;">+ extra lamb + 8</span><span class="price">30</span></li>
      <li class="dish" style="margin-bottom:12px;">Thai Chicken Curry <span class="chilli">&#9679;</span> <span class="note">mild</span> <span class="gfo">gfo</span><span class="note">traditional recipe, w/ jasmine rice &amp; papadums</span><span class="price">26</span></li>
      <li class="dish" style="margin-bottom:12px;">Beach Burger <span class="veg">v</span><span class="note">house-made pea &amp; corn ricotta fritter, pineapple, w/ wedges, onion rings, sweet chilli</span><span class="price">25</span></li>
      <li class="dish">Vegan Curry <span class="chilli">&#9679;</span> <span class="note">mild</span> <span class="gfo">gfo</span> <span class="veg">v</span><span class="note">chickpea &amp; pumpkin w/ fresh tomatoes &amp; basil, jasmine rice &amp; papadums</span><span class="price">24</span></li>
    </ul>
    <p class="turn-over">for PIZZA please see over......
      <svg width="18" height="12" viewBox="0 0 18 12" aria-hidden="true"><path d="M0 6h13M10 1l6 5-6 5" fill="none" stroke="var(--sun)" stroke-width="2.5"/></svg>
    </p>
    <div class="edge-band edge-band--bottom"></div>
  </section>

  <!-- Pizza side -->
  <section class="page page--pizza" aria-label="Pizza menu">
    <div class="edge-band edge-band--top"></div>
    <h1 class="page-title" style="font-size:66px; line-height:60px;">PIZZA</h1>
    <p class="pizza-sub">12" with house-made<br>tomato base &amp; mozzarella</p>
    <div class="food-art" role="img" aria-label="Illustration of three pizza slices" style="left:190px; top:56px; width:92px; height:50px; border-radius:8px; background:linear-gradient(90deg,#f6c04a,#e8553a,#f6c04a);"></div>
    <div class="shop-art" role="img" aria-label="Illustration of the colourful cafe shopfront" style="left:300px; top:34px; width:190px; height:80px;"></div>
    <div class="social" style="left:326px; top:118px;"><span class="social-dot"></span>@tidelinekitchen</div>

    <div class="legend-band" style="top:148px;">
      <p class="legend"><span class="veg-mark">v</span><span>Vegetarian</span><span class="gfo-mark gap">gfo</span><span>Gluten Friendly Optional, please ask</span></p>
    </div>

    <h2 class="allergy-head">ALLERGIES? PLEASE LET US KNOW!</h2>
    <p class="allergy-text">We are happy to cater for allergies including gluten, however our kitchen is small and we do not have separate preparation or cooking areas. As such, there is risk of cross contamination with your allergen and we are unable to guarantee allergen-free meals. Olives may very rarely contain pips.</p>
    <p class="sides">chips 8<b>|</b>greek salad 16<b>|</b>garden salad 12</p>

    <ul class="pizza-list">
      <li class="dish">Margherita <span class="veg">v</span><span class="note">tomato &amp; diced tomatoes, fresh basil</span></li>
      <li class="dish">BBQ Chicken<span class="note">chicken, tomato, spanish onion, bbq sauce</span></li>
      <li class="dish">Supreme<span class="note">ham, pepperoni, mushrooms, spanish onion</span> <span class="chilli">&#9679;</span></li>
      <li class="dish">Garden <span class="veg">v</span><span class="note">olives, roasted capsicum, mushrooms, spanish onion</span></li>
      <li class="dish">Hawaiian<span class="note">ham, pineapple, bbq sauce</span></li>
      <li class="dish">Mediterranean <span class="veg">v</span><span class="note">kalamata olives, roasted capsicum, parmesan</span></li>
      <li class="dish">Spicy Prawn<span class="note">prawns, spanish onion, chilli, tomato, mushrooms</span> <span class="chilli">&#9679;</span></li>
      <li class="dish">Build Your Own<span class="note">mozzarella &amp; four toppings</span></li>
    </ul>
    <p class="group-price" style="left:500px; top:410px;">22</p>
    <p class="group-price" style="left:500px; top:424px;">22</p>
    <ul class="pizza-list" style="top:560px;">
      <li class="dish">Carbonara<span class="note">cream base, bacon, spanish onion</span></li>
      <li class="dish">Pesto Chicken<span class="note">capsicum, chilli, spring onion, basil pesto</span> <span class="chilli">&#9679;</span></li>
      <li class="dish">Greek <span class="veg">v</span><span class="note">dried tomatoes, roasted capsicum, kalamata olives, spinach</span></li>
      <li class="dish">Chorizo<span class="note">chilli, chorizo, spanish onion</span> <span class="chilli">&#9679;&#9679;</span></li>
    </ul>
    <p class="group-price" style="left:488px; top:590px;">all 26</p>
    <p class="group-price" style="left:488px; top:756px;">all 29</p>
    <div class="edge-band edge-band--bottom"></div>
  </section>

</main>
</body>
</html>
```